Professional Business Card for Commercial Cleaning Company

We need a business card that represents our commercial janitorial cleaning company and represent several brands for our company so we do not want to highlight the logo too much. We want something that says we are professional.
Notes:No website or address as we have many locations and many websites and companies under our corporate name of "Brightvale Holdings, LLC" . Every time we hand a customer a business card they have contacted us via another brand we own but we don't want to have 21 business cards so we want to not focus on Brightvale Holdings, LLC too much since people will automatically ask "What is Brightvale Holdings, LLC" Example: Noodle Barn and Wrap Lantern restaurants are owned by "Zest! Brands" is the corporation name. Same principle here. Except we do not advertise at this time that all of our brands are connected. Hope this helps.
Target Market(s)
Commercial Cleaning
Industry/Entity Type
Janitorial Service
Contact Information for Business Card
Milo Jarvis
Business Development
555-382-9047
sales@brightvaleholdingsllc.example
Requirements
Must have
- Logo with contact information, need to be able to easily edit contact info for others in my office.
Nice to have
- Professional Image. Like to see a colorful bold look and a more standard business card look.
Should not have
- Any type of cleaning icons, tools, people or water.

```html
<!DOCTYPE html>
<html lang="en">
<head>
<meta charset="utf-8">
<title>Brightvale Holdings, LLC — Business Card</title>
<link rel="stylesheet" href="https://fonts.googleapis.com/css2?family=Montserrat:wght@600;700&family=Lato:wght@400&display=swap">
<style>
  :root {
    --page-bg: #e9e9e7;
    --card-white: #fbfbfb;
    --card-dark: #474747;
    --navy: #1f3b78;
    --steel-blue: #4d7db8;
    --ink: #333333;
    --shadow: rgba(0, 0, 0, 0.18);
  }
  * { box-sizing: border-box; margin: 0; padding: 0; }
  html, body {
    width: 1200px;
    height: 1200px;
    overflow: hidden;
    background: var(--page-bg);
  }
  .sheet {
    width: 1200px;
    height: 1200px;
    display: flex;
    flex-direction: column;
    align-items: center;
    justify-content: center;
    gap: 60px;
  }
  .card {
    position: relative;
    width: 900px;
    height: 514px;
    box-shadow: 0 8px 24px var(--shadow);
  }
  .card--back {
    background: var(--card-dark);
    display: flex;
    align-items: center;
    justify-content: center;
  }
  .card--front {
    background: var(--card-white);
  }
  .company-name {
    font-family: "Montserrat", sans-serif;
    font-weight: 700;
    letter-spacing: 0.2px;
    white-space: nowrap;
  }
  .card--back .company-name {
    color: var(--steel-blue);
    font-size: 52px;
  }
  .card--front .company-name {
    position: absolute;
    left: 78px;
    top: 92px;
    color: var(--navy);
    font-size: 44px;
  }
  .person {
    position: absolute;
    left: 70px;
    top: 352px;
  }
  .person__name {
    font-family: "Montserrat", sans-serif;
    font-weight: 700;
    font-size: 36px;
    color: var(--navy);
    text-transform: uppercase;
    letter-spacing: 0.3px;
    line-height: 1.1;
  }
  .person__title {
    font-family: "Lato", sans-serif;
    font-size: 20px;
    color: var(--ink);
    margin-top: 2px;
  }
  .contact {
    position: absolute;
    left: 440px;
    top: 404px;
    list-style: none;
    font-family: "Lato", sans-serif;
    font-size: 20px;
    color: var(--ink);
  }
  .contact__item {
    display: flex;
    align-items: center;
    gap: 14px;
    line-height: 1.45;
  }
  .contact__icon {
    width: 18px;
    height: 18px;
    flex: none;
    fill: var(--navy);
  }
</style>
</head>
<body>
<main class="sheet">
  <section class="card card--back" aria-label="Card back">
    <p class="company-name">Brightvale Holdings, LLC</p>
  </section>

  <section class="card card--front" aria-label="Card front">
    <p class="company-name">Brightvale Holdings, LLC</p>

    <div class="person">
      <p class="person__name">Milo Jarvis</p>
      <p class="person__title">Business Development</p>
    </div>

    <ul class="contact">
      <li class="contact__item">
        <svg class="contact__icon" viewBox="0 0 24 24" aria-hidden="true">
          <path d="M6.6 10.8a15.1 15.1 0 0 0 6.6 6.6l2.2-2.2a1 1 0 0 1 1-.25 11.4 11.4 0 0 0 3.6.57 1 1 0 0 1 1 1V20a1 1 0 0 1-1 1A17 17 0 0 1 3 4a1 1 0 0 1 1-1h3.5a1 1 0 0 1 1 1c0 1.25.2 2.45.57 3.57a1 1 0 0 1-.25 1z"/>
        </svg>
        <span>+555-382-9047</span>
      </li>
      <li class="contact__item">
        <svg class="contact__icon" viewBox="0 0 24 24" aria-hidden="true">
          <path d="M2 5h20v14H2z M4 7v.4l8 5.2 8-5.2V7z" fill-rule="evenodd"/>
        </svg>
        <span>sales@brightvaleholdingsllc.example</span>
      </li>
    </ul>
  </section>
</main>
</body>
</html>
```